Web Design Project

Psychotherapy and Counselling Practice needs a landing page web design.

My business "Larkspur Advisory" specialises in the treatment of Anxiety and Depression with a holistic approach, endeavouring to unlock the key that holds us to ransom in a life that is imbalanced, frustrating, and ultimately of our own making due to our own perceptions and behaviours.

There is much that impacts us which we cannot change, but we are always in control of how we think, and how we frame our experiences.....learning to challenge those thoughts and behaviours that are destructive and disempowering opens up a world of joyful possibility. Life is about making choices, learn to make wiser and healthier choices.......

Larkspur Advisory has a client base of individual clients but will seek to expand to offer services to the Corporate world by offering an adjunct to employers for established "Wellness Programs".

Larkspur Advisory is a highly professional, ethically bound business, with the needs of the client at the forefront of all we do.

Larkspur Advisory wishes to avoid the usual "jargon driven" psychobabble offered on many counselling web pages. It aims to be stylishly presented, clean in look and with as few "words" as possible and a largely white background (faster loading and more powerful impact of what is stated), those words contained in the webpage should be meaningful, persuasive and have an impact simply at glance. Larkspur does not want , or expect, those prospective clients in need of support , to be reading through volumes of industry driven cliches.

At this point Larkspur is just looking for a high quality landing page. However in time this will likely expand to include other sections such as case studies, video content etc.

Target Market(s)

Those in need of emotional support, suffering mental health issues, and those simply wanting to become self aware supported by a mindful therapist.

Industry/Entity Type

Industry

Requirements
Must have
• The design must incorporate the Larkspur logo and colour schemes found on the attached files.

```html
<!DOCTYPE html>
<html lang="en">
<head>
<meta charset="utf-8">
<title>Larkspur Advisory</title>
<link rel="stylesheet" href="https://fonts.googleapis.com/css2?family=Antonio:wght@100;400&family=Questrial&family=Open+Sans:wght@400;600;700&display=swap">
<style>
  :root {
    --green: #8aa812;
    --grey: #747474;
    --grey-dark: #6e6e6e;
    --grey-light: #9a9a9a;
    --rule: #dcd8d0;
    --white: #ffffff;
    --footer: #737373;
  }
  * { margin: 0; padding: 0; box-sizing: border-box; }
  html, body { width: 1200px; height: 1000px; overflow: hidden; background: var(--white); }
  body { position: relative; font-family: "Open Sans", sans-serif; color: var(--grey); }

  .main-nav { position: absolute; top: 32px; left: 507px; display: flex; align-items: center; font-family: "Questrial", sans-serif; font-size: 14px; }
  .main-nav a { color: var(--green); text-decoration: none; height: 27px; line-height: 27px; padding: 0 12px; margin-right: 15px; white-space: nowrap; }
  .main-nav a:last-child { margin-right: 0; padding-right: 0; }
  .main-nav a.is-active { background: var(--grey); color: var(--white); border-radius: 5px; margin-right: 15px; }
  .header-rule { position: absolute; top: 71px; left: 120px; width: 961px; height: 1px; background: var(--rule); }

  .vine-art { position: absolute; top: 90px; left: 262px; width: 76px; height: 584px; background: linear-gradient(180deg, #eef3dc, #dfe9bd 50%, #eef3dc); border-radius: 30px 30px 4px 4px; }
  .brand-name { position: absolute; top: 270px; left: 118px; width: 404px; text-align: center; font-family: "Questrial", sans-serif; font-size: 66px; letter-spacing: 3px; color: var(--green); line-height: 76px; }

  .quote { position: absolute; top: 113px; left: 540px; width: 530px; text-align: center; font-family: "Antonio", sans-serif; font-weight: 100; font-size: 52px; line-height: 60px; color: var(--grey); text-transform: uppercase; white-space: nowrap; }
  .quote .accent { color: var(--green); }
  .quote-author { position: absolute; top: 298px; left: 765px; width: 194px; height: 56px; }
  .quote-author span { position: absolute; top: 16px; left: 0; width: 194px; height: 39px; line-height: 39px; text-align: center; font-family: "Antonio", sans-serif; font-weight: 400; font-size: 17px; color: var(--white); text-transform: uppercase; letter-spacing: 0.5px; }

  .contact-card { position: absolute; top: 440px; left: 615px; width: 411px; text-align: center; font-family: "Open Sans", sans-serif; }
  .contact-card .tagline { font-size: 23px; height: 49px; line-height: 40px; color: var(--grey); }
  .contact-card .tagline b { color: var(--green); font-weight: 400; }
  .contact-card .rule { height: 1px; background: var(--rule); }
  .contact-card .call { font-size: 17px; color: var(--green); margin-top: 11px; line-height: 24px; }
  .contact-card .name { font-weight: 700; font-size: 24px; color: var(--grey); margin-top: 14px; line-height: 28px; }
  .contact-card .credentials { font-size: 11px; color: var(--grey-light); line-height: 14px; }
  .contact-card .line { font-weight: 600; font-size: 14px; color: var(--grey-dark); line-height: 22px; }
  .contact-card .line.first { margin-top: 16px; }
  .contact-card .rule.bottom { margin-top: 12px; }

  .footer-band { position: absolute; top: 674px; left: 0; width: 1200px; height: 20px; background: var(--green); }
  .site-footer { position: absolute; top: 694px; left: 0; width: 1200px; height: 88px; background: var(--footer); }
  .social { position: absolute; top: 11px; left: 137px; display: flex; gap: 13px; }
  .social span { width: 35px; height: 35px; border-radius: 50%; background: radial-gradient(circle at 50% 35%, #555, #2e2e2e); border: 1px solid #8a8a8a; }
  .copyright { position: absolute; top: 61px; left: 138px; font-size: 11px; color: var(--white); font-weight: 600; }
  .web-address { position: absolute; top: 22px; left: 662px; color: var(--green); font-size: 16px; white-space: nowrap; }
  .web-address b { font-weight: 400; font-size: 23px; }
</style>
</head>
<body>
  <nav class="main-nav">
    <a class="is-active" href="#">HOME</a>
    <a href="#">OUR SERVICES</a>
    <a href="#">CASE STUDY</a>
    <a href="#">WHO WE ARE</a>
    <a href="#">CONTACT US</a>
  </nav>
  <div class="header-rule"></div>

  <div class="vine-art" role="img" aria-label="Illustration of a climbing green vine with curling tendrils and leaves"></div>
  <div class="brand-name">LARKSPUR</div>

  <p class="quote">Just <span class="accent">living</span> is not enough. One<br><span class="accent">must have sunshine</span>, <span class="accent">freedom</span>,<br>and <span class="accent">a little flower</span>.</p>
  <div class="quote-author">
    <svg width="194" height="56" viewBox="0 0 194 56" aria-hidden="true">
      <polygon points="19,0 40,16 19,16" fill="#8aa812"/>
      <rect x="0" y="16" width="194" height="39" rx="5" fill="#8aa812"/>
    </svg>
    <span>Elsa Marwood</span>
  </div>

  <section class="contact-card">
    <div class="tagline"><b>Consulting</b> is highly Professional</div>
    <div class="rule"></div>
    <div class="call">Call Us Today:</div>
    <div class="name">MARA ELLISON</div>
    <div class="credentials">BA (Psych) BSc (Hons) Psych MBPS</div>
    <div class="line first">Mobile: 0412 555 018</div>
    <div class="line">E-mail: mara.ellison@larkmail.net</div>
    <div class="rule bottom"></div>
  </section>

  <div class="footer-band"></div>
  <footer class="site-footer">
    <div class="social"><span></span><span></span><span></span><span></span></div>
    <div class="copyright">Copyright © 2013 LARKSPUR - All rights reserved</div>
    <div class="web-address">www.<b>larkspuradvisory</b>.com.au</div>
  </footer>
</body>
</html>
```